Career Management Consultant Fun Professional Business Card

This is a business card for a personal career management consultant. The vibe needs to be professional but fun, modern with colour.

The name of the business is "Marcus Telwanger Career Management Consulting"

The name of the individual is "Marcus Telwanger" and his title is "Career Management Consultant"

Industry/Entity Type

Business

Contact Information for Business Card

Marcus Telwanger
Phone: 0400 827 316
Email: Marcus.Telwanger@mailvessa.com

```html
<!DOCTYPE html>
<html lang="en">
<head>
<meta charset="utf-8">
<title>Marcus Telwanger – Business Card</title>
<link rel="stylesheet" href="https://fonts.googleapis.com/css2?family=Tinos:wght@400;700&display=swap">
<style>
  :root {
    --backdrop: #d9dadc;
    --card: #f4f4f5;
    --card-edge: #e6e7e9;
    --sheen: rgba(255, 255, 255, 0.9);
    --brand-blue: #1c4f9a;
    --text-grey: #555a60;
    --icon-grey: #44484d;
  }
  * { box-sizing: border-box; margin: 0; padding: 0; }
  html, body {
    width: 1200px;
    height: 900px;
    overflow: hidden;
    background: var(--backdrop);
    font-family: "Tinos", "Times New Roman", serif;
  }
  .canvas {
    position: relative;
    width: 1200px;
    height: 900px;
    display: flex;
    flex-direction: column;
    align-items: center;
    justify-content: center;
    gap: 60px;
  }
  .card {
    position: relative;
    width: 630px;
    height: 360px;
    background: radial-gradient(ellipse at 50% 45%, #ffffff 0%, var(--card) 60%, var(--card-edge) 100%);
    box-shadow: 0 6px 18px rgba(0, 0, 0, 0.18);
    display: flex;
    flex-direction: column;
    align-items: center;
    justify-content: center;
    text-align: center;
    overflow: hidden;
  }
  .card__sheen {
    position: absolute;
    left: 0;
    width: 100%;
    height: 3px;
    background: linear-gradient(90deg, transparent 0%, var(--sheen) 35%, var(--sheen) 65%, transparent 100%);
  }
  .card__sheen--top { top: 40px; }
  .card__sheen--bottom { bottom: 56px; }

  /* Contact side */
  .contact__name {
    color: var(--brand-blue);
    font-weight: 700;
    font-size: 20px;
    margin-bottom: 6px;
  }
  .contact__line {
    display: flex;
    align-items: center;
    justify-content: center;
    gap: 8px;
    color: var(--text-grey);
    font-size: 19px;
    line-height: 1.45;
  }
  .contact__icon { flex: none; }

  /* Identity side */
  .identity__name {
    color: var(--brand-blue);
    font-weight: 700;
    font-size: 40px;
    letter-spacing: 0.5px;
    line-height: 1;
  }
  .identity__tagline {
    color: var(--text-grey);
    font-size: 22px;
    margin-top: 2px;
    letter-spacing: 0.3px;
  }
</style>
</head>
<body>
<main class="canvas">

  <section class="card card--contact" aria-label="Contact side">
    <span class="card__sheen card__sheen--top"></span>
    <h2 class="contact__name">Marcus Telwanger</h2>
    <p class="contact__line">
      <svg class="contact__icon" width="14" height="14" viewBox="0 0 14 14" aria-hidden="true">
        <circle cx="7" cy="7" r="6" fill="none" stroke="var(--icon-grey)" stroke-width="1.4"/>
        <path d="M4.6 3.6c-.9.9-.6 2.9 1 4.6s3.6 2 4.5 1.1l-1.3-1.3-1 .6c-.8-.4-1.7-1.3-2.1-2.1l.6-1-1.7-1.9z" fill="var(--icon-grey)"/>
      </svg>
      <span>0400 827 316</span>
    </p>
    <p class="contact__line">
      <svg class="contact__icon" width="22" height="15" viewBox="0 0 22 15" aria-hidden="true">
        <rect x="1" y="1" width="20" height="13" fill="none" stroke="var(--icon-grey)" stroke-width="1.3"/>
        <path d="M1 1l10 7 10-7M1 14l7-6M21 14l-7-6" fill="none" stroke="var(--icon-grey)" stroke-width="1.3"/>
      </svg>
      <span>Marcus.Telwanger@mailvessa.com</span>
    </p>
    <span class="card__sheen card__sheen--bottom"></span>
  </section>

  <section class="card card--identity" aria-label="Name side">
    <span class="card__sheen card__sheen--top"></span>
    <h1 class="identity__name">Marcus Telwanger</h1>
    <p class="identity__tagline">Career Management Consulting</p>
    <span class="card__sheen card__sheen--bottom"></span>
  </section>

</main>
</body>
</html>
```